基本レイアウトについては
https://zumelo.com/diagrams/XR8k21pTbvNDWfeL
もしくは、添付データのワイヤーをご参照ください。
レイアウトについては必ずしも上記に準じている必要はありません。
ご自由にご提案いただいても結構です。

全体の雰囲気としては
http://www.tomirei-wedding.net/
http://www.hokumorisanjingu.or.jp/
のような、桜色をつかいながら
あまり古臭くなり過ぎないようにアピールできればと思います。

また、製品は
http://www.seiryu-kojin.co.jp/goods/luvasystem
http://www.gw-tmr.co.jp/
のものを使用しています。

美容室へ来られる方は、近隣の方が多く、
和髪以外での競争力はあまりないため、WEB上では
美容師への和髪の講習などの訴求時に、
信頼性を高めるような用途が多くなりそうです。

そのため、上記参考サイトのような
ちょっとしたスタイリッシュさを目指しています。
http://qrvmd.ozu.ne.jp/0597214483/index.html
ホワイト、桜色をベースに、落ち着いた印象に出来ればと存じます。
素材については、
下記URLよりダウンロードしたものをご利用いただければ幸甚です。
http://plumvault.jp/download/a4f19e02bd7753c6e1088f2d94ab37c51e0d2a96

こちらだけですと、制作が難しいと思いますので
http://mobre.jp/
などから、5000円程度までならこちらにて購入可能です。カンプデータにて作成頂き、
納品時に当方にて購入したデータに差し替えていただければと存じます。

【参考サイト】
↑色合い、印象が気に入っています

http://www.gw-tmr.co.jp/
↑使用している製品のホームページです

http://basement-parts.com/2012/166.html
http://basement-parts.com/2011/115.html
↑フッター部分の参照です

基本レイアウト
については、必ずしも忠実である必要はありません。

是非ご提案お待ちしております。
何卒よろしくお願いいたします。

クライアント様との協議の結果こちらの案を採用させていただきました。
上品さと柔らかさのバランスがとてもよく、
視認性も高く、要望を全て満たしておりましたので
こちらの案を採用いたしました。

この度は多数ご提案いただきありがとうございました。
当選に至らなかったランサー様におかれましては大変心苦しいのですが、
またの機会にぜひご提案いただければ幸甚です。
引き続き何卒よろしくお願いいたします。

```html
<!DOCTYPE html>
<html lang="ja">
<head>
<meta charset="utf-8">
<title>ミツバ美容室</title>
<link rel="stylesheet" href="https://fonts.googleapis.com/css2?family=Noto+Sans+JP:wght@400;700&family=Noto+Serif+JP:wght@400;600&display=swap">
<style>
:root{
  --pink:#c07a98;
  --pink-deep:#a95d80;
  --pink-soft:#f4e6ec;
  --pink-pale:#faf3f6;
  --ink:#4a4346;
  --muted:#8a8286;
  --line:#e3d3da;
  --footer:#4d4a4b;
  --footer-deep:#3e3b3c;
  --white:#ffffff;
}
*{box-sizing:border-box;margin:0;padding:0}
html,body{width:774px;height:1200px;overflow:hidden;background:var(--white)}
body{font-family:"Noto Sans JP",sans-serif;color:var(--ink);font-size:10px;position:relative}
.serif{font-family:"Noto Serif JP",serif}

.site-header{height:46px;display:flex;align-items:center;justify-content:space-between;padding:0 22px;border-bottom:1px solid var(--line)}
.brand{display:flex;flex-direction:column;gap:2px}
.brand-name{display:flex;align-items:center;gap:6px;font-family:"Noto Serif JP",serif;font-size:14px;color:var(--pink-deep)}
.brand-dot{width:12px;height:12px;border-radius:50%;background:var(--pink)}
.brand-sub{font-size:7px;color:var(--muted)}
.header-tel{display:flex;align-items:center;gap:6px;font-size:15px;font-weight:700;color:var(--ink)}
.tag{background:var(--pink);color:var(--white);font-size:8px;padding:2px 5px;font-weight:400}

.hero{position:relative;height:306px;display:flex}
.hero-photo{width:460px;height:100%;background:linear-gradient(115deg,#2b2226 0%,#6a4d5a 40%,#b89aa8 70%,#e8dce2 100%)}
.hero-copy{position:absolute;left:140px;top:120px;color:var(--white);font-family:"Noto Serif JP",serif}
.hero-copy .big{font-size:34px;letter-spacing:4px;line-height:1.25;text-shadow:0 1px 3px rgba(0,0,0,.35)}
.hero-copy .small{font-size:10px;margin-top:8px;letter-spacing:2px}
.hero-panel{flex:1;background:linear-gradient(180deg,var(--pink-soft),var(--pink-pale));display:flex;padding:34px 18px;gap:16px}
.hero-brand{display:flex;flex-direction:column;gap:10px;width:120px}
.hero-brand .brand-name{font-size:17px}
.vertical{writing-mode:vertical-rl;font-family:"Noto Serif JP",serif;font-size:11px;color:var(--pink-deep);letter-spacing:3px;margin-top:12px}
.hero-products{flex:1;margin-top:40px;background:linear-gradient(180deg,#ffffff,#e9dde2);border-radius:2px}

.global-nav{display:flex;gap:6px;padding:14px 20px 0}
.global-nav a{flex:1;height:56px;border:1px solid var(--pink);display:flex;flex-direction:column;align-items:center;justify-content:center;gap:5px;color:var(--pink-deep);text-decoration:none;font-size:9px;background:var(--white)}
.global-nav a.current{background:var(--pink);color:var(--white)}
.nav-icon{width:16px;height:16px;border-radius:50%;border:1.5px solid currentColor}

.main{display:flex;gap:20px;padding:22px 20px 0}
.sidebar{width:180px;display:flex;flex-direction:column;gap:12px}
.contact-box{border:1px solid var(--line);padding:12px 10px;text-align:left}
.contact-box .lead{font-size:8px;color:var(--muted)}
.contact-box .tel{font-size:19px;font-weight:700;margin:4px 0 2px;color:var(--ink)}
.contact-box p{font-size:8px;line-height:1.6}
.side-menu{list-style:none;border-top:1px solid var(--line)}
.side-menu li{display:flex;justify-content:space-between;align-items:center;height:32px;border-bottom:1px solid var(--line);padding:0 8px;font-size:9px}
.side-menu li::after{content:"›";color:var(--pink);font-size:13px}
.side-banner{position:relative;height:120px;background:linear-gradient(135deg,#6d5560,#c7a7b5 60%,#efe3e8);display:flex;align-items:center;padding-left:14px}
.side-banner span{font-family:"Noto Serif JP",serif;color:var(--white);font-size:13px;line-height:1.5}

.content{flex:1;display:flex;flex-direction:column;gap:22px}
.section-title{display:flex;align-items:center;gap:8px;font-family:"Noto Serif JP",serif;font-size:12px;color:var(--ink);border-bottom:2px solid var(--pink);padding-bottom:6px}
.section-title::before{content:"";width:10px;height:10px;border-radius:50%;background:var(--pink)}
.news-list{list-style:none}
.news-list li{display:flex;align-items:center;gap:12px;height:28px;border-bottom:1px dotted var(--line);font-size:8.5px}
.news-date{background:#8d8689;color:var(--white);font-size:7.5px;padding:2px 6px}
.more{align-self:flex-end;background:#8d8689;color:var(--white);font-size:8px;padding:3px 10px;margin-top:-14px}
.welcome{display:flex;gap:14px}
.welcome-text{flex:1;font-size:8.5px;line-height:1.8}
.welcome-products{width:160px;height:130px;background:linear-gradient(180deg,#fbfbfb,#dfd8db)}
.shop-row{display:flex;gap:14px}
.shop-photo{width:130px;height:90px;background:linear-gradient(180deg,#5f6a4a,#8b8f6a 55%,#b7b3a6)}
.shop-row p{flex:1;font-size:8.5px;line-height:1.8}

.page-top{position:absolute;right:24px;top:1002px;background:var(--pink);color:var(--white);font-size:8px;padding:4px 10px}

.site-footer{position:absolute;left:0;bottom:0;width:100%;height:170px;background:var(--footer);color:#e8e2e5;padding:22px 40px 0;display:flex;justify-content:space-between}
.footer-links{display:grid;grid-template-columns:repeat(2,110px);row-gap:8px;list-style:none;font-size:8.5px;align-content:start}
.footer-links li::before{content:"› ";color:var(--pink)}
.footer-info{text-align:right;display:flex;flex-direction:column;gap:6px;align-items:flex-end}
.footer-info .brand-name{color:var(--white);font-size:18px}
.footer-info .addr{font-size:10px}
.footer-info .header-tel{color:var(--white);font-size:15px}
.copyright{position:absolute;left:0;bottom:0;width:100%;height:22px;background:var(--footer-deep);font-size:7px;display:flex;align-items:center;justify-content:center;color:#bdb5b9}
</style>
</head>
<body>

<header class="site-header">
  <div class="brand">
    <div class="brand-name"><span class="brand-dot"></span>ミツバ美容室</div>
    <div class="brand-sub">静岡県浜松市の和髪・着付け専門 美容室 日本髪と振袖の着付け</div>
  </div>
  <div class="header-tel"><span>059-721-4483</span><span class="tag">要予約</span></div>
</header>

<section class="hero">
  <div class="hero-photo" role="img" aria-label="日本髪を結った和装の女性の後ろ姿の写真"></div>
  <div class="hero-copy">
    <div class="big">日本の心と<br>女性美</div>
    <div class="small">伝統の和髪を、今の女性へ。</div>
  </div>
  <div class="hero-panel">
    <div class="hero-brand">
      <div class="brand-name"><span class="brand-dot"></span>ミツバ美容室</div>
      <div class="vertical">伝統の技を、未来へ。</div>
    </div>
    <div class="hero-products" role="img" aria-label="店で使用しているヘアケア製品のボトルの写真"></div>
  </div>
</section>

<nav class="global-nav">
  <a class="current" href="#"><span class="nav-icon"></span>ホーム</a>
  <a href="#"><span class="nav-icon"></span>ヘアー・料金</a>
  <a href="#"><span class="nav-icon"></span>着付け・料金</a>
  <a href="#"><span class="nav-icon"></span>講習会のご案内</a>
  <a href="#"><span class="nav-icon"></span>よくある質問</a>
  <a href="#"><span class="nav-icon"></span>お問合せ</a>
</nav>

<div class="main">
  <aside class="sidebar">
    <div class="contact-box">
      <div class="lead">お電話でお気軽にご相談ください</div>
      <div class="tel">059-721-4483</div>
      <p>（平日 9:00〜18:00）<br>火曜・第1・3水曜定休<br>臨時休業有・要予約</p>
    </div>
    <ul class="side-menu">
      <li>ホーム</li>
      <li>ヘアー・料金</li>
      <li>着付け・料金</li>
      <li>よくある質問</li>
      <li>お問合せ</li>
    </ul>
    <div class="side-banner" role="img" aria-label="和髪の講習風景の写真"><span>和髪の技術<br>学びませんか？</span></div>
  </aside>

  <main class="content">
    <section>
      <h2 class="section-title">新着情報</h2>
      <ul class="news-list">
        <li><span class="news-date">2014.02.10</span>春の振袖着付けのご予約受付を開始しました</li>
        <li><span class="news-date">2014.01.28</span>美容師向け和髪講習会の日程を掲載しました</li>
        <li><span class="news-date">2014.01.15</span>成人式の着付けにご来店ありがとうございました</li>
        <li><span class="news-date">2013.12.20</span>年末年始の営業日についてのお知らせです</li>
        <li><span class="news-date">2013.12.02</span>新しいヘアケア製品の取り扱いを始めました</li>
        <li><span class="news-date">2013.11.18</span>七五三の日本髪セットのご案内を更新しました</li>
      </ul>
    </section>
    <span class="more">一覧表示</span>

    <section>
      <h2 class="section-title">ミツバ美容室へようこそ</h2>
      <div class="welcome" style="margin-top:12px">
        <p class="welcome-text">ミツバ美容室は地域の皆さまに長く愛されてきた和髪専門の美容室です。日本髪の結い上げから振袖の着付けまで、伝統の技を大切に一人ひとりに丁寧に仕上げます。<br><br>厳選したヘアケア製品を使用し、髪と頭皮にやさしい施術を心がけております。美容師の方へ向けた和髪の講習も行っております。</p>
        <div class="welcome-products" role="img" aria-label="店で取り扱うヘアケア製品の写真"></div>
      </div>
    </section>
    <div class="shop-row">
      <div class="shop-photo" role="img" aria-label="美容室の外観の写真"></div>
      <p>お店は駅から歩いて数分の静かな通りにございます。ご来店の際は事前にお電話でご予約ください。</p>
    </div>
  </main>
</div>

<span class="page-top">ページトップ</span>

<footer class="site-footer">
  <ul class="footer-links">
    <li>ホーム</li><li>講習会</li>
    <li>ヘアー・料金</li><li>プライバシーポリシー</li>
    <li>着付け・料金</li><li></li>
    <li>よくある質問</li><li></li>
    <li>お問合せ</li><li></li>
  </ul>
  <div class="footer-info">
    <div class="brand-name"><span class="brand-dot"></span>ミツバ美容室</div>
    <div class="addr">静岡県浜松市中区元城町3-14-7</div>
    <div class="header-tel"><span>059-721-4483</span><span class="tag">要予約</span></div>
  </div>
  <div class="copyright">Copyright (C) 2014 ミツバ美容室 All Rights Reserved.</div>
</footer>

</body>
</html>
```